Ebook/Booklet Cover: Neue Arbeitswelten
Tolles Miteinander, hat genau gefühlt und erkannt wo ich hin wollte. Und war sehr geduldig, da ich die letzten Informationen zum Buch jetzt erst mit großer Verspätung übermitteln konnte. Gerne jederzeit wieder!
Zielgruppe
Beratung und Training für kleine und mittlere Unternehmen im Bereich Arbeitnehmerschutz (Arbeitssicherheit), Stressprävention und Aufbau von alltagstauglichen Arbeitsabläufen/Strukturen.
In diesem Buchprojekt jetzt trete ich jedoch nicht primär als Unternehmen auf, sondern als Autorin.
Zielgruppe: Bis jetzt Führungskräfte, Geschäftsführer, Personalmanagement in Unternehmen.
Das soll auch so bleiben nur ist mein Plan in Zukunft auch Privatpersonen anzusprechen.
Inhalt des Ebooks:
Ratgeber, Impulsgeber und Informationsvermittler zu den Themen 'Hybrides Arbeiten', 'Arbeiten im Home Office', 'Digitales Arbeiten' .
Einzelne Themen sind jeweils in einem eigenen Ebook.
Titel ist noch in Arbeit. Es sollten jedoch 2 Zeilen sein.
Eines welches das Thema grob beschreibt - zB 'Perspektiven zur Arbeitswelt der Zukunft' (Das bleibt immer gleich) und darunter 'Hybrides Arbeiten' (Das ist bei jedem Thema dann extra)
Es geht inhaltlich darum, welche Folgen haben diese neuen Arbeitssituationen für Körper - Geist und Psyche und wie geht man im Idealfall damit um. Und wie bereiten wir uns für diese enormen Veränderungen in der ZUkunft optimal vor.
Mit dem Ziel, dass sich der Leser Tipps rauspickt die er selbst umsetzen kann zu Hause. Und vielleicht auch eine neue Perspektive in diese neue Arbeitswelt bekommt.
Und auch Unternehmer und Personalverantwortliche haben so einen Leitfaden für die Zukunft.
Man könnte sagen 'Hoch wissenschaftliche Inhalte + gesetzliche Vorgaben (Also teilweise komplizierte + trockene Inhalte) sollen niederschwellig, leicht lesbar und unterhaltsam präsentiert werden.
Aufgabenstellung
Ich mag Klares. Sauberes. Harmonisches. Ein Mix aus 'edel, niveauvoll, professionell' und 'sympathisch, fröhlich, stylisch'
Nichts Überladenes, keine Reizüberflutung.
Und es darf ein klein wenig darf 'Spiritualität' durchkommen - muss aber nicht.
Auf meiner Homepage sieht man eine Kugel zwischen 2 Händen. Diese passt zB sehr gut zu mir: Verbindend, harmonisch, klar, 'rund'.
Ich habe diese Velmora Bildarchiv Datei angefügt - muss aber nicht verwendet werden!
Weiter unten, wo der Regler zu verschieben ist um Vorstellungen einzugrenzen ist mir aufgefallen, dass dies gar nicht so einfach so beschreiben ist ;-). Wenn eine klare Struktur da ist (zB weißer Hintergrund), Farben harmonisch sind darf ein Teil gerne verspielt und bunt sein als Akzent. Aber eben nicht chaotisch überladen.
Vom Typ her bin ich eher 'HIN ZU statt WEG VON'. Ein Buchcover zum Thema 'Durch Entspannung weniger Stress' würde bei mir zB keinen Kopf zeigen der Blitze und Chaos um sich hat. Sondern ein Kopf der entspannte, bunte, fließende Gedanken hat.
Mei, ich hoffe Ihr Kreativen die das lest habt Eure Kristallkugel zum Gedankenlesen dabei,... ist gar nicht so einfach meine Vorstellung in Worte zu fassen :-).
Zur Preisgestaltung in dem Projekt: Ich bin (Wie viele von uns) finanziell recht gebeutelt durch die aktuelle Situation. Daher geht aktuell nur das Minibudget.
Ich plane hier aber Schritt für Schritt mehr zu machen (Als Autorin) in Zukunft und es ist absolut die Möglichkeit einer weiteren Zusammenarbeit vorhanden.
Liebe Grüße an Euch alle!!
Update:
zu viel schwarze Farbe ist nicht so meines ;-), - ich tendiere zu hellen Designs...

```html
<!DOCTYPE html>
<html lang="de">
<head>
<meta charset="utf-8">
<title>Hybrides Arbeiten – Buchumschlag</title>
<link rel="stylesheet" href="https://fonts.googleapis.com/css2?family=Bebas+Neue&family=Oswald:wght@500;600&family=Roboto:ital,wght@0,300;0,400;1,300&display=swap">
<style>
  :root {
    --stage: #8a8886;
    --mint: #b9e1dd;
    --mint-deep: #a2c8c5;
    --orange: #e35a0e;
    --orange-deep: #c84f0c;
    --slate: #3f5c6d;
    --white: #ffffff;
    --photo-grey: #c9c9cb;
    --illustration: #c78a5c;
  }
  * { box-sizing: border-box; margin: 0; padding: 0; }
  html, body { width: 1200px; height: 800px; overflow: hidden; }
  body {
    background: var(--stage);
    display: flex;
    align-items: center;
    justify-content: center;
    font-family: "Roboto", Arial, sans-serif;
  }
  .book-wrap {
    display: flex;
    height: 560px;
    box-shadow: 0 14px 36px rgba(0,0,0,.28);
  }

  /* Back cover */
  .back-cover {
    position: relative;
    width: 372px;
    background: linear-gradient(90deg, var(--mint) 0%, var(--mint) 70%, var(--mint-deep) 100%);
  }
  .author-photo {
    position: absolute;
    z-index: 1;
    left: 36px; top: 52px;
    width: 78px; height: 138px;
    background: linear-gradient(180deg, var(--photo-grey) 0%, #b5aca6 60%, #efefef 100%);
  }
  .blurb-panel {
    position: absolute;
    left: 70px; top: 96px;
    width: 254px; height: 412px;
    background: linear-gradient(135deg, var(--orange) 0%, var(--orange-deep) 100%);
    color: var(--white);
    padding: 108px 16px 0 16px;
    font-size: 8.6px;
    line-height: 1.38;
  }
  .blurb-panel p { margin-bottom: 9px; text-align: justify; hyphens: auto; }
  .blurb-call {
    margin-top: 12px;
    text-align: center;
    font-size: 10.5px;
    line-height: 1.3;
    text-transform: uppercase;
  }
  .blurb-call span { display: block; margin-bottom: 6px; }

  /* Spine */
  .spine {
    width: 44px;
    background: linear-gradient(90deg, var(--orange-deep), var(--orange) 40%, var(--orange-deep));
    color: var(--white);
    display: flex;
    flex-direction: column;
    align-items: center;
    padding: 30px 0 16px;
  }
  .spine-text {
    writing-mode: vertical-rl;
    transform: rotate(180deg);
    display: flex;
    align-items: center;
    gap: 40px;
    flex: 1;
    justify-content: center;
    white-space: nowrap;
  }
  .spine-title {
    font-family: "Oswald", "Arial Narrow", sans-serif;
    font-weight: 600;
    font-style: italic;
    font-size: 27px;
    letter-spacing: .5px;
  }
  .spine-subtitle {
    font-family: "Oswald", "Arial Narrow", sans-serif;
    font-weight: 500;
    font-style: italic;
    font-size: 15px;
  }
  .spine-author {
    font-size: 9.5px;
    text-align: center;
    line-height: 1.2;
  }

  /* Front cover */
  .front-cover {
    position: relative;
    width: 372px;
    background: linear-gradient(180deg, var(--mint) 0%, var(--mint-deep) 100%);
    padding: 26px 26px 0 34px;
    text-align: right;
  }
  .cover-title {
    font-family: "Bebas Neue", "Oswald", "Arial Narrow", sans-serif;
    font-weight: 400;
    color: var(--orange);
    line-height: .9;
    letter-spacing: 2px;
    white-space: nowrap;
    font-size: 100px;
  }
  .cover-title.line-two { margin-top: 4px; }
  .cover-subtitle {
    font-family: "Roboto", Arial, sans-serif;
    font-weight: 300;
    color: var(--slate);
    white-space: nowrap;
  }
  .cover-subtitle.line-one { font-size: 18px; }
  .cover-subtitle.line-two { font-size: 19px; }
  .cover-author {
    font-size: 11px;
    color: var(--slate);
    margin-top: 2px;
  }
  .cover-illustration {
    position: absolute;
    left: 28px; right: 28px;
    top: 318px; height: 176px;
    background: radial-gradient(ellipse at 55% 55%, var(--illustration) 0%, rgba(199,138,92,.55) 45%, rgba(162,200,197,0) 80%);
    border-radius: 8px;
  }
  .cover-tagline {
    position: absolute;
    left: 28px; right: 24px; bottom: 22px;
    font-size: 10px;
    font-weight: 300;
    font-style: italic;
    color: var(--slate);
    text-align: left;
    line-height: 1.35;
    letter-spacing: .4px;
  }
</style>
</head>
<body>
  <div class="book-wrap">
    <section class="back-cover">
      <div class="author-photo" role="img" aria-label="Porträtfoto der Autorin"></div>
      <div class="blurb-panel">
        <p>Dank „Politik klar gesagt“ werden Sie beim Lesen von Nachrichten nicht mehr von Überlegungen abgelenkt, was diese oder jene Begriffe zu bedeuten haben.</p>
        <p>Sie bilden außerdem faktenbasiert eine eigene, gut begründete Meinung und können politische Diskussionen auf Augenhöhe verfolgen und sogar souverän führen.</p>
        <p>Sie erkennen die Probleme der aktuellen Politik und können somit frühzeitig erkennen was für berufliche wie private Folgen auf Ihr Leben haben könnte.</p>
        <p>Mit Ihrem Wissen können Sie andere Menschen aufklären und für die Zusammenhänge der aktuellen Lage begeistern.</p>
        <div class="blurb-call">
          <span>Worauf warten Sie noch?</span>
          <span>Gestalten Sie jetzt<br>unsere Zukunft mit!</span>
        </div>
      </div>
    </section>

    <section class="spine">
      <div class="spine-text">
        <span class="spine-title">HYBRIDES ARBEITEN</span>
        <span class="spine-subtitle">Arbeiten im Home Office</span>
      </div>
      <div class="spine-author">Marlene<br>Winter</div>
    </section>

    <section class="front-cover">
      <h1 class="cover-title line-one">HYBRIDES</h1>
      <p class="cover-subtitle line-one">Digitales Arbeiten</p>
      <h1 class="cover-title line-two">ARBEITEN</h1>
      <p class="cover-subtitle line-two">Arbeiten im Home Office</p>
      <p class="cover-author">Marlene Winter</p>
      <div class="cover-illustration" role="img" aria-label="Illustration: Frau im Home Office am Schreibtisch, ein Vorgesetzter schaut aus dem Bildschirm, Uhr und Pflanze im Hintergrund"></div>
      <p class="cover-tagline">Ein Ratgeber, Impulsgeber und Informationsvermittler für Führungskräfte, Geschäftsführer und Personalmanagement</p>
    </section>
  </div>
</body>
</html>
```